Business Profile Landing Page for search engine Start UP " Ember Gate"

Hi there
Ember Gate is an search engine for the Ember Gate - business.

What i´m looking for is a stunning singel Profile Landing Page for the Companys presentation.

Following Details should be included.

1st section
Comapanys name
Adress
info row ( opening time or what ever)
Profile Picture Big ( Could be the logo)
+3 smaller Pictures ( Maybe the store, main product ...)

2nd Section
navigation Icons for:
Call, Mail , Web, Route, Data

3er Section
About us.

Text lines.....
+Pictures slider

4th Section
1 row : Products ( Titel , Picture, Price)
2nd row :Service ( same as Products + text lines )

5th section
Blog Posts row

.....................................................
Well thats all, Colors used from the logo, u can also use the favicon somewhere (the crown magnifying glass)

Target Market(s)

All Comapnys, it should be an " used for all" design

Number of Pages Required

1 page

Requirements
Must have
• The first sighting is the important part, so the " first section should be impressively and makes the customers curious about more informations (very important for mobile version)
Nice to have
• If you can insert our favicon somewhere would be cool, but its not nessesery
Should not have
• you dont need to make a header or footer, that part is already done. i just need the main section design

```html
<!DOCTYPE html>
<html lang="en">
<head>
<meta charset="utf-8">
<title>Ember Gate – Business Profile</title>
<link href="https://fonts.googleapis.com/css2?family=Poppins:wght@400;500;600;700&family=Open+Sans:wght@400;600&display=swap" rel="stylesheet">
<style>
:root{
  --gold:#f5b800;
  --gold-soft:#ffd04d;
  --ink:#1d1a17;
  --dark:#221d19;
  --brown:#4a302b;
  --text:#3a3a3a;
  --muted:#8a8a8a;
  --line:#e6e6e6;
  --white:#ffffff;
  --peach:#f7a98a;
}
*{box-sizing:border-box;margin:0;padding:0}
html,body{width:1200px;height:3524px;overflow:hidden}
body{
  position:relative;
  font-family:"Open Sans",Arial,sans-serif;
  color:var(--text);
  background:linear-gradient(180deg,#0e0c0b 0,#1a1613 700px,#2c241d 1000px,#4a3e33 1150px,#8f877e 1400px,#f4f2ef 1750px,#ffffff 1950px);
}
.abs{position:absolute}
h1,h2,h3,h4{font-family:"Poppins",Arial,sans-serif}

/* HERO */
.hero-photo{left:0;top:0;width:1200px;height:560px;background:linear-gradient(160deg,#6b5a4a 0%,#3b3129 40%,#141110 100%)}
.hero-shade{left:0;top:0;width:1200px;height:560px;background:linear-gradient(180deg,rgba(0,0,0,.1),rgba(14,12,11,.92))}
.hero-brand{left:0;top:150px;width:1200px;text-align:center;font-family:"Poppins",sans-serif;font-weight:600;font-size:52px;line-height:1;color:var(--white);display:flex;justify-content:center;align-items:center;gap:20px}
.hero-brand .dot{width:64px;height:64px;border-radius:50%;background:var(--gold)}
.hero-intro{left:360px;top:340px;width:480px;text-align:center;color:#e8e3dc;font-size:13px;line-height:21px}
.info-row{left:0;top:406px;width:1200px;display:flex;justify-content:center}
.info-item{width:300px;text-align:center;color:#d9d4cc;font-size:12px}
.info-item svg{display:block;margin:0 auto 14px}
.scroll-btn{left:582px;top:508px}

.gallery{top:584px;height:316px}
.g1{left:80px;width:340px;background:linear-gradient(135deg,#8d8a86,#3c3b3a)}
.g2{left:432px;width:336px;background:linear-gradient(135deg,#e0d5c6,#6f5f4f)}
.g3{left:784px;width:336px;background:linear-gradient(180deg,#7fa7d6,#cfd9e2 60%,#7b6f64)}
.g1 span{position:absolute;left:40px;top:138px;color:var(--white);font-family:"Poppins",sans-serif;font-weight:600;font-size:28px}

.nav{left:0;top:956px;width:1200px;display:flex;justify-content:center;gap:72px}
.nav-item{width:92px;text-align:center}
.nav-icon{width:76px;height:76px;margin:0 auto;border-radius:50%;border:2px solid #6a625a;display:flex;align-items:center;justify-content:center}
.nav-label{margin-top:30px;height:26px;border:1px solid #6a625a;border-radius:6px;font-size:11px;line-height:24px;color:#bdb5ab}
.nav-item.is-active .nav-icon{background:var(--gold);border-color:var(--gold)}
.nav-item.is-active .nav-label{background:var(--gold);border-color:var(--gold);color:var(--ink);font-weight:600}

/* ABOUT */
.arc{left:-260px;top:1150px;width:1720px;height:1500px;border-radius:50%;background:var(--white)}
.brand-mark{left:0;top:1205px;width:1200px;text-align:center}
.brand-mark .name{font-family:"Poppins",sans-serif;font-weight:700;font-size:40px;color:var(--ink);display:inline-flex;align-items:center;gap:12px}
.brand-mark .name i{width:16px;height:16px;background:var(--gold);border-radius:50%;display:inline-block}
.brand-mark .sub{font-family:"Poppins",sans-serif;font-weight:500;font-size:26px;color:var(--ink);margin-top:2px}
.about-photo{left:380px;top:1330px;width:360px;height:360px;border-radius:50%;background:radial-gradient(circle at 50% 45%,#e5ded6,#b8aa9b 60%,#8b7c6c)}
.ring-deco{left:540px;top:1350px;width:300px;height:300px;border-radius:50%;border:44px solid #f1f1f1}
.bubble-a{left:760px;top:1440px;width:76px;height:76px;border-radius:50%;background:linear-gradient(135deg,#ffc9ad,var(--peach))}
.bubble-b{left:356px;top:1620px;width:100px;height:100px;border-radius:50%;background:linear-gradient(135deg,#ffe3cc,#fbb58f)}

.features{left:160px;top:1770px;width:880px;display:flex;gap:60px}
.feature{width:253px}
.feature .num{font-family:"Poppins",sans-serif;font-weight:600;font-size:34px;color:var(--gold);line-height:1}
.feature h3{font-size:22px;font-weight:600;color:var(--gold);margin:4px 0 18px}
.feature p{font-size:12px;line-height:20px;color:var(--muted)}

.slider .slide{position:absolute}
.s1{left:0;top:2070px;width:260px;height:250px;background:linear-gradient(135deg,#d8d4cd,#8b8680)}
.s2{left:320px;top:2050px;width:560px;height:290px;background:linear-gradient(135deg,#c9a37a,#6b4a33 60%,#2c2622)}
.s3{left:920px;top:2070px;width:280px;height:250px;background:linear-gradient(180deg,#cfe0ee,#8fae72 55%,#9c9a97)}

/* PLANS */
.plans-bg{left:180px;top:2330px;width:840px;height:620px;border-radius:50%;background:#f6f6f6}
.section-title{left:0;width:1200px;text-align:center;font-family:"Poppins",sans-serif;font-weight:600;font-size:28px;color:var(--gold)}
.plan{top:2470px;width:260px;height:420px;background:var(--white);border-radius:10px;box-shadow:0 10px 30px rgba(0,0,0,.1);text-align:center;padding-top:120px}
.plan-a{left:296px}.plan-b{left:632px}
.plan-pic{position:absolute;left:70px;top:-50px;width:120px;height:120px;border-radius:50%;border:6px solid var(--gold)}
.plan-a .plan-pic{background:linear-gradient(135deg,#f2e3c8,#b9885a)}
.plan-b .plan-pic{background:linear-gradient(135deg,#9ab3c9,#3b4a5a)}
.plan h3{font-size:26px;font-weight:600;color:var(--gold);line-height:30px}
.plan .desc{font-size:11px;line-height:17px;color:var(--muted);margin:14px 40px 20px}
.plan .price{font-family:"Poppins",sans-serif;font-weight:600;font-size:44px;color:var(--ink);line-height:1}
.plan .per{font-size:12px;color:var(--muted);margin-top:4px}
.btn{display:inline-block;background:var(--gold);color:var(--ink);font-family:"Poppins",sans-serif;font-weight:600;font-size:11px;border-radius:20px}
.plan .btn{margin-top:26px;width:100px;height:30px;line-height:30px}

/* BLOG */
.blog{left:80px;top:3000px;width:1040px;display:flex;gap:20px}
.post{width:245px}
.post .img{height:150px;border-radius:4px}
.p1 .img{background:linear-gradient(135deg,#7a2a26,#c9b9a8)}
.p2 .img{background:linear-gradient(135deg,#9fb4c8,#2d3a4a)}
.p3 .img{background:linear-gradient(135deg,#b88a5c,#3d2f27)}
.p4 .img{background:linear-gradient(135deg,#d9cfc0,#7a6a58)}
.post .cat{font-size:9px;color:var(--gold);font-weight:600;margin:14px 0 6px;text-transform:uppercase}
.post h4{font-size:15px;font-weight:600;line-height:19px;color:var(--ink);height:58px}
.post p{font-size:10px;line-height:15px;color:var(--muted);margin-top:8px}
.read-more{left:980px;top:3362px;font-size:11px;color:var(--gold);font-weight:600}

/* NEWSLETTER */
.newsletter{left:0;top:3400px;width:1200px;height:124px;background:var(--brown)}
.newsletter h2{position:absolute;left:140px;top:44px;font-size:26px;font-weight:600;color:var(--white)}
.newsletter .field{position:absolute;left:600px;top:48px;width:310px;height:30px;border-radius:16px;background:var(--white);font-size:11px;color:#aaa;line-height:30px;padding-left:18px}
.newsletter .btn{position:absolute;left:930px;top:48px;width:120px;height:30px;line-height:30px;text-align:center}
</style>
</head>
<body>

<!-- HERO -->
<div class="abs hero-photo" role="img" aria-label="Photo of hands typing on a laptop at a desk"></div>
<div class="abs hero-shade"></div>
<div class="abs hero-brand"><span class="dot"></span>Ember Gate</div>
<p class="abs hero-intro">Vienna, Austria's capital, lies in the country's east on the Danube River. Its artistic and intellectual legacy was shaped by residents including the city's composers and thinkers.</p>

<div class="abs info-row">
  <div class="info-item">
    <svg width="18" height="22" viewBox="0 0 18 22"><path d="M9 1a7 7 0 0 0-7 7c0 5 7 13 7 13s7-8 7-13a7 7 0 0 0-7-7z" fill="var(--gold)"/><circle cx="9" cy="8" r="2.6" fill="#1d1a17"/></svg>
    Lindenweg 19, Vienna 1010 Austria
  </div>
  <div class="info-item">
    <svg width="22" height="22" viewBox="0 0 22 22"><circle cx="11" cy="11" r="9" fill="none" stroke="var(--gold)" stroke-width="2.4"/><path d="M11 6v5l3.5 2.5" fill="none" stroke="var(--gold)" stroke-width="2.2" stroke-linecap="round"/></svg>
    10 am – 08 pm
  </div>
  <div class="info-item">
    <svg width="22" height="22" viewBox="0 0 24 24"><path d="M6.6 10.8a15 15 0 0 0 6.6 6.6l2.2-2.2c.3-.3.7-.4 1-.2 1.1.4 2.300.6 3.6.6.6 0 1 .4 1 1V20c0 .6-.4 1-1 1A17 17 0 0 1 3 4c0-.6.4-1 1-1h3.5c.6 0 1 .4 1 1 0 1.3.2 2.5.6 3.6.1.3 0 .7-.2 1z" fill="var(--gold)"/></svg>
    +43 660 555 0199
  </div>
</div>
<svg class="abs scroll-btn" width="36" height="36" viewBox="0 0 36 36"><circle cx="18" cy="18" r="18" fill="var(--gold)"/><path d="M11 15l7 7 7-7" fill="none" stroke="#1d1a17" stroke-width="3" stroke-linecap="round"/></svg>

<div class="abs gallery g1" role="img" aria-label="Photo of the store building front"><span>Store</span></div>
<div class="abs gallery g2" role="img" aria-label="Photo of a hand holding a smartphone"></div>
<div class="abs gallery g3" role="img" aria-label="Photo of a cathedral tower over city rooftops"></div>

<nav class="abs nav">
  <div class="nav-item">
    <div class="nav-icon"><svg width="28" height="28" viewBox="0 0 24 24"><path d="M6.6 10.8a15 15 0 0 0 6.6 6.6l2.2-2.2c.3-.3.7-.4 1-.2 1.1.4 2.3.6 3.6.6.6 0 1 .4 1 1V20c0 .6-.4 1-1 1A17 17 0 0 1 3 4c0-.6.4-1 1-1h3.5c.6 0 1 .4 1 1 0 1.3.2 2.5.6 3.6.1.3 0 .7-.2 1z" fill="none" stroke="#8d847a" stroke-width="1.5"/></svg></div>
    <div class="nav-label">Call</div>
  </div>
  <div class="nav-item">
    <div class="nav-icon"><svg width="30" height="24" viewBox="0 0 30 24"><rect x="2" y="3" width="26" height="18" rx="2" fill="none" stroke="#8d847a" stroke-width="1.6"/><path d="M3 5l12 9 12-9" fill="none" stroke="#8d847a" stroke-width="1.6"/></svg></div>
    <div class="nav-label">Mail</div>
  </div>
  <div class="nav-item is-active">
    <div class="nav-icon"><svg width="32" height="28" viewBox="0 0 32 28"><rect x="2" y="3" width="28" height="22" rx="2" fill="none" stroke="#1d1a17" stroke-width="2"/><path d="M2 9h28" stroke="#1d1a17" stroke-width="2"/><rect x="7" y="13" width="18" height="3" fill="#1d1a17"/><rect x="7" y="19" width="12" height="2" fill="#1d1a17"/></svg></div>
    <div class="nav-label">Website</div>
  </div>
  <div class="nav-item">
    <div class="nav-icon"><svg width="24" height="30" viewBox="0 0 24 30"><path d="M12 2a9 9 0 0 0-9 9c0 7 9 17 9 17s9-10 9-17a9 9 0 0 0-9-9z" fill="none" stroke="#8d847a" stroke-width="1.6"/><circle cx="12" cy="11" r="3.5" fill="none" stroke="#8d847a" stroke-width="1.6"/></svg></div>
    <div class="nav-label">Route</div>
  </div>
  <div class="nav-item">
    <div class="nav-icon"><svg width="24" height="30" viewBox="0 0 24 30"><path d="M3 2h12l6 6v20H3z" fill="none" stroke="#8d847a" stroke-width="1.6"/><path d="M7 14h10M7 19h10M7 24h6" stroke="#8d847a" stroke-width="1.6"/></svg></div>
    <div class="nav-label">Data</div>
  </div>
</nav>

<!-- ABOUT -->
<div class="abs arc"></div>
<div class="abs brand-mark">
  <div class="name"><i></i>Ember Gate</div>
  <div class="sub">Floristen &amp; Gärtner</div>
</div>
<div class="abs ring-deco"></div>
<div class="abs about-photo" role="img" aria-label="Photo of two colleagues talking over a laptop"></div>
<div class="abs bubble-a"></div>
<div class="abs bubble-b"></div>

<section class="abs features">
  <div class="feature">
    <div class="num">01</div>
    <h3>Experience</h3>
    <p>Vienna, Austria's capital, lies in the country's east on the Danube River. Its artistic and intellectual legacy was shaped by residents of every era and trade.</p>
  </div>
  <div class="feature">
    <div class="num">02</div>
    <h3>Highlights</h3>
    <p>The city is also known for its imperial palaces, including the summer residence, and its museum quarter with historic and contemporary buildings nearby.</p>
  </div>
  <div class="feature">
    <div class="num">03</div>
    <h3>Services</h3>
    <p>Until the beginning of the 20th century, Vienna was the largest German-speaking city in the world, and before the splitting of the empire had two million inhabitants.</p>
  </div>
</section>

<div class="slider">
  <div class="slide s1" role="img" aria-label="Photo of a city street with shop fronts"></div>
  <div class="slide s2" role="img" aria-label="Photo of a person working on a laptop at a wooden table"></div>
  <div class="slide s3" role="img" aria-label="Photo of a tree-lined street with a tram"></div>
</div>

<!-- PLANS -->
<div class="abs plans-bg"></div>
<h2 class="abs section-title" style="top:2372px">Select Your Plan</h2>
<div class="abs plan plan-a">
  <div class="plan-pic" role="img" aria-label="Photo of a person holding a product"></div>
  <h3>Special<br>Offer</h3>
  <p class="desc">Save up to $80 when you subscribe on a yearly plan.</p>
  <div class="price">$250</div>
  <div class="per">/ years</div>
  <span class="btn">BUY NOW</span>
</div>
<div class="abs plan plan-b">
  <div class="plan-pic" role="img" aria-label="Photo of a hand holding a phone"></div>
  <h3>Full<br>Services</h3>
  <p class="desc">Every tool, every listing and full support for companies.</p>
  <div class="price">$1250</div>
  <div class="per">/ years</div>
  <span class="btn">BUY NOW</span>
</div>

<!-- BLOG -->
<h2 class="abs section-title" style="top:2944px">Our Blog</h2>
<section class="abs blog">
  <article class="post p1">
    <div class="img" role="img" aria-label="Photo of a speaker at a conference"></div>
    <div class="cat">Tips &amp; Guides</div>
    <h4>Searchly Offers Details on Core Update Recovery Times</h4>
    <p>A new post explains how long sites may wait to see rankings return after an update.</p>
  </article>
  <article class="post p2">
    <div class="img" role="img" aria-label="Photo of a presenter on a stage"></div>
    <div class="cat">News</div>
    <h4>Orchard Ratings is coming to Orbit OS 14: how disruptive will it be?</h4>
    <p>Local shops may soon see ratings shown directly inside maps and search results.</p>
  </article>
  <article class="post p3">
    <div class="img" role="img" aria-label="Photo of people viewing paintings in a gallery"></div>
    <div class="cat">Tips &amp; Guides</div>
    <h4>Art lovers beware: All exhibitions you should not miss in Vienna</h4>
    <p>From classic halls to new spaces, these shows are worth a visit this season.</p>
  </article>
  <article class="post p4">
    <div class="img" role="img" aria-label="Photo of a busy street with cafés"></div>
    <div class="cat">Tips &amp; Guides</div>
    <h4>French flair in the Servitenviertel</h4>
    <p>Quiet lanes, small bakeries and shops give this quarter a charm of its own.</p>
  </article>
</section>
<div class="abs read-more">VIEW MORE →</div>

<!-- NEWSLETTER -->
<section class="abs newsletter">
  <h2>Subscribe our Newsletter</h2>
  <div class="field">Your e-mail</div>
  <span class="btn">SUBSCRIBE</span>
</section>

</body>
</html>
```